Refresh existing website - qfamdv.org

Apply these upgrades to the existing website
1. Modern Design: Update the overall aesthetic to a clean, contemporary look with bold typography,
vibrant colors, and improved visual hierarchy.
2. Mobile Optimization: Enhance responsiveness for seamless navigation on mobile devices.
3. Intuitive User Interface: Simplify navigation by reducing menu complexity and improving call-to-
action buttons.
4. SEO Optimization: Improve content for better ranking on search engines.
5. Accessibility: Ensure compliance with WCAG standards for inclusivity.
6. Faster Load Times: Optimize images and scripts for better performance.
7. Social Media Integration: Add live social media feeds to showcase community engagement.
8. Prefer html
Industry/Entity Type
Consulting
Coding
Coded - Design and coding required
Number of Pages Required
5+ page
Look and feel

```html
<!DOCTYPE html>
<html lang="en">
<head>
<meta charset="utf-8">
<title>QFAMDV – Quality Forum of Advisors in Medical &amp; Dental Ventures</title>
<link href="https://fonts.googleapis.com/css2?family=Roboto:wght@400;500;700&display=swap" rel="stylesheet">
<style>
:root{
  --green:#7cb02c;
  --green-dark:#6a9a22;
  --ink:#222;
  --body:#444;
  --muted:#777;
  --line:#ddd;
  --blue:#3e6a93;
  --pale:#eaeff4;
  --foot:#3b3e41;
  --white:#fff;
}
*{box-sizing:border-box;margin:0;padding:0}
html,body{width:1200px;height:3851px;overflow:hidden}
body{font-family:'Roboto',Arial,sans-serif;color:var(--body);background:var(--white);position:relative}
.abs{position:absolute}
a{color:inherit;text-decoration:none}
.btn{position:absolute;display:flex;align-items:center;justify-content:center;background:var(--green);color:var(--white);font-weight:700;font-size:15px;text-transform:uppercase}
.btn::after{content:"";position:absolute;left:5px;top:5px;right:-5px;bottom:-5px;border:1px solid var(--green);pointer-events:none}
.btn.light::after{border-color:#fff}
.eyebrow{color:var(--green);font-size:20px;text-transform:uppercase}
.heading{color:var(--ink);font-weight:500;font-size:33px;text-transform:uppercase}
.photo{position:absolute}

/* header */
.site-header{position:absolute;left:0;top:0;width:1200px;height:107px;background:#fff}
.logo{position:absolute;left:75px;top:28px;width:168px;height:57px;display:flex;align-items:center;justify-content:center;font-weight:700;font-size:30px;color:#2f3b45;letter-spacing:1px}
.toplinks{position:absolute;top:24px;left:420px;display:flex;font-size:15px;color:#555}
.toplinks span{padding:0 18px;border-left:1px solid #999;line-height:20px}
.toplinks span:first-child{border:0}
.login{left:958px;top:15px;width:165px;height:38px;font-size:15px}
.login::after{display:none}
.nav{position:absolute;top:66px;left:282px;display:flex;gap:28px;font-size:15px;color:#444}
.nav .active{color:var(--green);text-decoration:underline}

/* hero */
.hero{position:absolute;left:0;top:107px;width:1200px;height:600px;background:linear-gradient(90deg,#3d4348 0%,#5b646b 35%,#9aa6ae 60%,#cfd5d9 100%)}
.hero h1{position:absolute;left:103px;top:155px;color:#fff;font-weight:400}
.hero .h-small{font-size:29px;display:block}
.hero .h-big{font-size:42px;font-weight:500;display:block;line-height:52px;margin-top:6px}
.hero p{position:absolute;left:103px;top:305px;width:455px;color:#fff;font-size:14px;line-height:22px}
.arrow{position:absolute;width:16px;height:16px;border-radius:50%;background:#fff}
.arrow svg{display:block}

/* about */
.about-text{position:absolute;left:640px;top:833px;width:450px}
.about-text p{font-size:13px;line-height:22.5px;margin-top:18px}

/* services */
.services-band{position:absolute;left:0;top:1287px;width:1200px;height:380px;background:linear-gradient(135deg,#8cbd3a,#6fa42b)}
.center{position:absolute;left:0;width:1200px;text-align:center}
.card{position:absolute;top:1677px;width:296px;height:265px;background:#fff;border:1px solid var(--line);padding:18px 16px}
.card h3{font-size:19px;font-weight:500;color:var(--ink);line-height:29px}
.card p{font-size:14px;line-height:23px;margin-top:8px}
.card.feature{background:var(--green);border-color:var(--green);color:#fff}
.card.feature h3{color:#fff}
.card .btn{left:16px;bottom:20px;width:136px;height:40px}
.card.feature .btn{background:#fff;color:var(--ink)}
.card.feature .btn::after{border-color:#fff}

/* clients */
.client{position:absolute;top:2213px;width:190px;height:71px;border:1px solid var(--line);background:#fff;display:flex;align-items:center;justify-content:center;font-size:22px;font-weight:500;color:#35536b}

/* foundation */
.foundation{position:absolute;left:0;top:2364px;width:1200px;height:602px;background:linear-gradient(120deg,#4d7aa3,#3b6389 55%,#2e5478)}
.found-text{position:absolute;left:640px;top:2500px;width:460px;color:#fff}
.found-text h4{font-size:20px;font-weight:500;margin-top:14px}
.found-text p{font-size:13px;line-height:23px;margin-top:2px}

/* contact */
.contact{position:absolute;left:0;top:2966px;width:1200px;height:454px;background:var(--pale)}
.field{position:absolute;background:#fff;border:1px solid #e2e6ea;font-size:13px;color:#666;padding:14px 16px}

/* footer */
.footer{position:absolute;left:0;top:3420px;width:1200px;height:431px;background:var(--foot);color:#fff}
.divider{position:absolute;top:100px;width:2px;height:280px;background:#fff}
.fcol h5{font-size:15px;font-weight:700;text-transform:uppercase}
.fcol ul{list-style:none;margin-top:22px}
.fcol li{font-size:14px;height:30px;display:flex;align-items:center;gap:22px}
.fcol li svg{flex:none}
.info{display:flex;gap:16px;margin-top:20px;font-size:11px;line-height:20px}
.info b{font-size:13px}
.social{position:absolute;top:230px;width:34px;height:34px;border:1.5px solid #fff;border-radius:50%}
</style>
</head>
<body>

<header class="site-header">
  <div class="logo" style="border:1.5px solid #5b6770">QFAMDV</div>
  <div class="toplinks"><span>Get Certified (QCA)</span><span>Find A Consultant</span><span>Consultant Current</span></div>
  <a class="btn login">Member Login</a>
  <nav class="nav"><a class="active">Home</a><a>About the Society</a><a>About Membership</a><a>Products/Services</a><a>Upcoming Education</a><a>Practice Reports</a><a>More ▾</a></nav>
</header>

<section class="hero" role="img" aria-label="Doctors and a consultant walking through a hospital corridor discussing a tablet">
  <h1><span class="h-small">QUALITY FORUM OF ADVISORS IN</span><span class="h-big">MEDICAL &amp; DENTAL<br>VENTURES</span></h1>
  <p>For nearly 30 years, the Quality Forum of Advisors in Medical &amp; Dental Ventures (QFAMDV) and its originating organizations have provided an active forum for networking and knowledge sharing.</p>
  <a class="btn light" style="left:103px;top:393px;width:140px;height:42px">Get Started</a>
  <span class="arrow" style="left:58px;top:300px"><svg width="16" height="16"><path d="M10 4 6 8l4 4" stroke="#444" stroke-width="2" fill="none"/></svg></span>
  <span class="arrow" style="left:1137px;top:300px"><svg width="16" height="16"><path d="M6 4l4 4-4 4" stroke="#444" stroke-width="2" fill="none"/></svg></span>
</section>

<div class="photo" role="img" aria-label="Two doctors reviewing a tablet together" style="left:105px;top:810px;width:426px;height:373px;background:linear-gradient(135deg,#7d8a98,#b9c4cf 55%,#dfe5ea)"></div>
<div class="about-text">
  <div class="eyebrow">About Us</div>
  <h2 class="heading" style="line-height:40px;margin-top:6px">The Quality Forum of Advisors in Medical &amp; Dental Ventures</h2>
  <p>The Quality Forum of Advisors in Medical &amp; Dental Ventures (QFAMDV) was founded July 1st, 2006. Its history began when members of the Institute of Practice Advisory Fellows, the Allied Association of Clinic Advisors, and the Society of Clinic Management Advisors came together to form one society to best serve practices across all fields.</p>
</div>
<a class="btn" style="left:640px;top:1132px;width:138px;height:43px">Read More</a>

<div class="services-band" role="img" aria-label="Green healthcare technology background"></div>
<div class="center" style="top:1350px;color:#fff;font-size:20px">PRODUCTS</div>
<div class="center heading" style="top:1378px;color:#fff">Our Services</div>

<div class="photo" role="img" aria-label="Senior couple meeting with a consultant" style="left:105px;top:1455px;width:311px;height:282px;background:linear-gradient(160deg,#c9b8a4,#8d7a66)"></div>
<div class="photo" role="img" aria-label="Medical staff watching a video presentation" style="left:445px;top:1455px;width:311px;height:282px;background:linear-gradient(160deg,#f1f3f4,#c7ccd0)"></div>
<div class="photo" role="img" aria-label="Doctor using digital network technology" style="left:786px;top:1455px;width:311px;height:282px;background:linear-gradient(160deg,#2d6f8e,#8fc3d6)"></div>

<article class="card" style="left:113px">
  <h3>Medicare Quarterly Updates Webinars</h3>
  <p>Our goal at QFAMDV is to research and interpret the rules, updates and Medicare alerts. We strive to make it easier for providers, clients, and healthcare professionals,</p>
  <a class="btn">Learn More</a>
</article>
<article class="card feature" style="left:453px">
  <h3>QFAMDV Presentation Videos</h3>
  <p>2023 Annual Conference Videos<br>2023 Winter Workshop Videos<br>2022 Behavioral Health and Mental Health Virtual Summit Videos<br>2022 Annual Conference Videos</p>
  <a class="btn">Learn More</a>
</article>
<article class="card" style="left:794px">
  <h3>Practice Benchmarks Reports</h3>
  <p>Each year the Society surveys its members' clients and compiles a Benchmarks Report on Medical and Dental Income and Expense Averages.</p>
  <a class="btn">Learn More</a>
</article>
<a class="btn" style="left:527px;top:1980px;width:141px;height:40px">View More</a>

<div class="center eyebrow" style="top:2115px">Meet Our Happy Clients</div>
<div class="center heading" style="top:2143px">Our Clients</div>
<span class="arrow" style="left:58px;top:2241px;background:var(--green)"><svg width="16" height="16"><path d="M10 4 6 8l4 4" stroke="#fff" stroke-width="2" fill="none"/></svg></span>
<span class="arrow" style="left:1137px;top:2241px;background:#222"><svg width="16" height="16"><path d="M6 4l4 4-4 4" stroke="#fff" stroke-width="2" fill="none"/></svg></span>
<div class="client" style="left:103px">Veranta Billing</div>
<div class="client" style="left:303px">Norvale</div>
<div class="client" style="left:506px">Clinivo</div>
<div class="client" style="left:707px">Triaxis</div>
<div class="client" style="left:908px">Halden</div>

<section class="foundation" role="img" aria-label="Blue background with a stethoscope and digital network overlay"></section>
<div class="photo" role="img" aria-label="Doctor and nurse looking at a tablet" style="left:105px;top:2462px;width:320px;height:328px;background:linear-gradient(150deg,#b9a999,#5b7da3)"></div>
<div class="photo" role="img" aria-label="Stethoscope resting on a laptop keyboard" style="left:320px;top:2640px;width:240px;height:225px;background:linear-gradient(150deg,#e6ebef,#8e9ba6);border:7px solid #2a4763"></div>
<div class="found-text">
  <div class="eyebrow">The Foundation for Learning in</div>
  <div style="font-size:31px;font-weight:500;text-transform:uppercase">Practice Administration</div>
  <h4>Mission :</h4>
  <p>The Foundation for Learning in Practice Administration is a non-profit organization dedicated to improving healthcare delivery through the education of practice management consultants.</p>
  <h4>Sponsored Methods of Education :</h4>
  <p>The most common sponsor options are meetings and seminars, publications, audio and videotapes, and human resources networks.</p>
</div>
<a class="btn" style="left:640px;top:2783px;width:140px;height:40px">Donate</a>

<section class="contact">
  <div class="center eyebrow" style="top:90px">Get In Touch</div>
  <div class="center heading" style="top:118px">Contact Us</div>
  <div class="field" style="left:190px;top:179px;width:264px;height:46px">Full Name</div>
  <div class="field" style="left:464px;top:179px;width:264px;height:46px">Phone</div>
  <div class="field" style="left:737px;top:179px;width:264px;height:46px">Email Address</div>
  <div class="field" style="left:190px;top:234px;width:811px;height:88px">Message</div>
  <a class="btn" style="left:522px;top:374px;width:142px;height:40px">Submit</a>
</section>

<footer class="footer">
  <div class="logo" style="left:88px;top:180px;width:194px;height:63px;color:#fff;border:1.5px solid #fff">QFAMDV</div>
  <span class="divider" style="left:317px"></span>
  <span class="divider" style="left:532px"></span>
  <span class="divider" style="left:740px"></span>
  <div class="fcol abs" style="left:353px;top:115px">
    <h5>Quick Links</h5>
    <ul>
      <li><svg width="14" height="12"><rect x="1" y="1" width="10" height="10" fill="none" stroke="#fff"/><path d="M3 6l3 3 7-8" stroke="#fff" stroke-width="1.6" fill="none"/></svg><u>Home</u></li>
      <li><svg width="14" height="12"><rect x="1" y="1" width="10" height="10" fill="none" stroke="#fff"/><path d="M3 6l3 3 7-8" stroke="#fff" stroke-width="1.6" fill="none"/></svg>About the Society</li>
      <li><svg width="14" height="12"><rect x="1" y="1" width="10" height="10" fill="none" stroke="#fff"/><path d="M3 6l3 3 7-8" stroke="#fff" stroke-width="1.6" fill="none"/></svg>About Membership</li>
      <li><svg width="14" height="12"><rect x="1" y="1" width="10" height="10" fill="none" stroke="#fff"/><path d="M3 6l3 3 7-8" stroke="#fff" stroke-width="1.6" fill="none"/></svg>Products/Services</li>
      <li><svg width="14" height="12"><rect x="1" y="1" width="10" height="10" fill="none" stroke="#fff"/><path d="M3 6l3 3 7-8" stroke="#fff" stroke-width="1.6" fill="none"/></svg>Upcoming Education</li>
      <li><svg width="14" height="12"><rect x="1" y="1" width="10" height="10" fill="none" stroke="#fff"/><path d="M3 6l3 3 7-8" stroke="#fff" stroke-width="1.6" fill="none"/></svg>Practice Reports</li>
      <li><svg width="14" height="12"><rect x="1" y="1" width="10" height="10" fill="none" stroke="#fff"/><path d="M3 6l3 3 7-8" stroke="#fff" stroke-width="1.6" fill="none"/></svg>More ▾</li>
    </ul>
  </div>
  <div class="fcol abs" style="left:555px;top:115px;width:170px">
    <h5>Contact Info</h5>
    <div class="info"><svg width="12" height="14"><path d="M6 1a4 4 0 0 1 4 4c0 3-4 8-4 8S2 8 2 5a4 4 0 0 1 4-4z" fill="#fff"/><circle cx="6" cy="5" r="1.5" fill="#3b3e41"/></svg><div><b>ADDRESS:</b><br>4820 Meridian Park Ln.<br>#212 Arden, VA 20341</div></div>
    <div class="info"><svg width="12" height="14"><path d="M2 2l3-1 2 3-2 2a8 8 0 0 0 3 3l2-2 3 2-1 3C6 12 1 7 2 2z" fill="#fff"/></svg><div><b>PHONE:</b><br>555-014-2290</div></div>
    <div class="info"><svg width="14" height="12"><rect x="1" y="2" width="12" height="9" fill="#fff"/><path d="M1 2l6 5 6-5" stroke="#3b3e41" fill="none"/></svg><div><b>EMAIL:</b><br>info@qfamdv.org</div></div>
  </div>
  <div class="fcol abs" style="left:765px;top:115px">
    <h5>Sign Up To Our Newsletter</h5>
  </div>
  <div class="abs" style="left:766px;top:183px;width:264px;height:42px;background:#fff;color:#555;font-size:13px;padding:13px 16px">Email Address
    <svg class="abs" style="right:14px;top:14px" width="14" height="14"><path d="M1 7l12-6-4 12-2-5z" fill="#7cb02c"/></svg></div>
  <span class="social" style="left:766px;background:#fff" aria-label="Social profile"></span>
  <span class="social" style="left:807px" aria-label="Social profile"></span>
  <span class="social" style="left:848px" aria-label="Social profile"></span>
  <span class="social" style="left:892px" aria-label="Social profile"></span>
  <div class="abs" style="left:120px;top:392px;width:910px;border-top:1px solid #55595d"></div>
  <div class="center" style="top:403px;font-size:12px">© 2024 QFAMDV | &nbsp; All Rights Reserved</div>
</footer>

</body>
</html>
```